Hip surgeon needs a educative book cover design

I need to re-design my old book cover for its 3rd edition.
It's a small book dedicated to my patients, who underwent total hip replacement. It's meant to help people getting around the basic care after a total hip replacement surgery and getting back to their normal, active life.
The title is: "Bright mornings: a walking companion guide".
I already had a new logo, new stationery and new website design from PixelHarbor (please see the attachments).
The final design should be look alike the other fresh new designs. It must communicate health, peacefulness.
I also attached the manual as it looks today for reference.
A5 size.
Just cover and back cover.

```html
<!DOCTYPE html>
<html lang="en">
<head>
<meta charset="utf-8">
<title>Bright Mornings – Book Cover</title>
<link href="https://fonts.googleapis.com/css2?family=Open+Sans:wght@400;600&family=Roboto+Condensed:wght@400&family=Montserrat:wght@700&family=Varela+Round&display=swap" rel="stylesheet">
<style>
  :root {
    --white: #ffffff;
    --ink: #2b2b2b;
    --title-blue: #1f5c9c;
    --bright-blue: #1a7cc4;
    --band-blue: #2263a3;
    --band-edge: #1d87c9;
    --runner-light: #2e8fd6;
    --runner-dark: #1862a8;
  }
  * { margin: 0; padding: 0; box-sizing: border-box; }
  html, body { width: 1200px; height: 818px; overflow: hidden; background: var(--white); }
  .cover { position: relative; width: 1200px; height: 818px; background: var(--white); font-family: "Open Sans", sans-serif; overflow: hidden; }

  .bottom-band { position: absolute; left: 0; top: 531px; width: 1200px; height: 287px; background: var(--band-blue); border-top: 6px solid var(--band-edge); }

  /* back cover */
  .author-photo { position: absolute; left: 52px; top: 46px; width: 97px; height: 135px; background: linear-gradient(160deg, #d9d4cc, #f1efea 55%, #c8c3bb); box-shadow: 0 1px 4px rgba(0,0,0,.35); border: 3px solid var(--white); }
  .brand { position: absolute; display: flex; align-items: center; gap: 8px; font-family: "Roboto Condensed", sans-serif; }
  .brand-dot { width: 30px; height: 30px; border-radius: 50%; background: var(--bright-blue); flex: none; }
  .brand-name { font-size: 21px; color: var(--bright-blue); }
  .brand--back { left: 172px; top: 42px; }
  .brand--back .brand-name { color: var(--title-blue); }
  .bio { position: absolute; left: 172px; top: 108px; width: 347px; font-size: 11px; line-height: 17.2px; color: var(--ink); text-align: justify; }
  .bio p + p { margin-top: 8px; }
  .code-box { position: absolute; left: 48px; top: 651px; width: 190px; height: 66px; background: var(--white); }
  .website { position: absolute; left: 48px; top: 729px; font-size: 15px; color: var(--white); }

  /* spine */
  .spine-edition { position: absolute; left: 590px; top: 0; width: 20px; height: 125px; background: var(--bright-blue); color: var(--white); writing-mode: vertical-rl; font-family: "Varela Round", sans-serif; font-size: 12px; text-align: center; padding-top: 40px; }
  .spine-title { position: absolute; left: 590px; top: 145px; writing-mode: vertical-rl; color: var(--title-blue); white-space: nowrap; }
  .spine-title strong { font-family: "Montserrat", sans-serif; font-size: 15px; letter-spacing: .5px; }
  .spine-title span { font-family: "Varela Round", sans-serif; font-size: 14px; margin-top: 10px; display: inline-block; }
  .spine-brand { position: absolute; left: 588px; top: 612px; display: flex; flex-direction: column; align-items: center; gap: 6px; }
  .spine-brand .brand-dot { width: 24px; height: 24px; background: var(--white); }
  .spine-brand .brand-name { writing-mode: vertical-rl; font-family: "Roboto Condensed", sans-serif; font-size: 15px; color: var(--white); }

  /* front cover */
  .edition-tag { position: absolute; left: 624px; top: 37px; width: 179px; height: 30px; background: var(--bright-blue); color: var(--white); font-family: "Varela Round", sans-serif; font-size: 18px; letter-spacing: 1px; display: flex; align-items: center; justify-content: center; }
  .book-title { position: absolute; right: 62px; top: 100px; text-align: right; font-family: "Montserrat", sans-serif; font-weight: 700; font-size: 60px; line-height: 66px; color: var(--title-blue); letter-spacing: 1px; }
  .book-subtitle { position: absolute; right: 62px; top: 230px; font-family: "Varela Round", sans-serif; font-size: 24px; color: var(--bright-blue); }
  .runner-art { position: absolute; left: 900px; top: 278px; width: 170px; height: 430px; }
  .brand--front { left: 690px; top: 719px; }
  .brand--front .brand-dot { width: 44px; height: 44px; background: var(--white); }
  .brand--front .brand-name { color: var(--white); font-size: 22px; }
</style>
</head>
<body>
<main class="cover">
  <div class="bottom-band"></div>

  <!-- back cover -->
  <div class="author-photo" role="img" aria-label="Portrait photo of the author in a white coat"></div>
  <div class="brand brand--back"><span class="brand-dot"></span><span class="brand-name">Dr. Lucas M. Ferreira</span></div>
  <div class="bio">
    <p>Physician trained USCL - Southern Coastal State University, specialist in Orthopedics and Traumatology with improvement in Hip Surgery in Brazil and abroad, Titular Member SOTA - National Society of Orthopaedics and Trauma, Titular Member of the SHJ - National Society of Hip and Joint, Member the IAJS - International Academy of Joint Surgeons.</p>
    <p>Secretary of SHJ / SC, Commissioner of Education and Training SOTA / SC, Full Member of the Technical Chamber of Orthopaedics, RMC / SC. currently exercises its functions in Lagoa Azul / SC, with special interest in hip arthroplasty (prostheses ), Arthroscopic Hip Surgery (Video by surgery, minimally invasive) and Trauma of Pelvis and Acetabulum.</p>
  </div>
  <div class="code-box"></div>
  <div class="website">www.hipcarejourney.com.br</div>

  <!-- spine -->
  <div class="spine-edition">3rd Edition</div>
  <div class="spine-title"><strong>BRIGHT MORNINGS</strong> <span>A Walking Companion Guide</span></div>
  <div class="spine-brand"><span class="brand-dot"></span><span class="brand-name">Dr. Lucas M. Ferreira</span></div>

  <!-- front cover -->
  <div class="edition-tag">3rd Edition</div>
  <h1 class="book-title">BRIGHT<br>MORNINGS</h1>
  <div class="book-subtitle">A Walking Companion Guide</div>
  <svg class="runner-art" viewBox="0 0 170 430" role="img" aria-label="Blue silhouette of a man running with a highlighted hip implant, casting a long shadow">
    <defs>
      <linearGradient id="runnerTone" x1="0" y1="0" x2="0" y2="1">
        <stop offset="0" stop-color="var(--runner-light)"/>
        <stop offset="1" stop-color="var(--runner-dark)" stop-opacity=".6"/>
      </linearGradient>
    </defs>
    <rect x="0" y="0" width="170" height="430" rx="60" fill="url(#runnerTone)" opacity=".85"/>
  </svg>
  <div class="brand brand--front"><span class="brand-dot"></span><span class="brand-name">Dr. Lucas M. Ferreira</span></div>
</main>
</body>
</html>
```